Selka Marven Photography Business Card

I need a new business card/ possibly design to use for other marking materials ... I have included my logo below in a few different colors, but can also provide the logo in additional colors and sizes. I would love a card the expresses clean, simple and classy.

Target Market(s)

Portrait photography clients, child photography clients

Industry/Entity Type

Photographer

Contact Information for Business Card

Selka Marven Photography, Braintree MA, www.selkamarvenphotography-demo.com
T. 555-203-1946 E. selkamarvenphoto@mailbox-demo.com

Colors
33b8a4
eea4c8
5c5c5c

Requirements
Must have
• I would like to include my logo on card.
Nice to have
• I also like the color brown as well as the choices below. I would like a simple, elegant card, something classy.

```html
<!DOCTYPE html>
<html lang="en">
<head>
<meta charset="utf-8">
<title>Selka Marven Photography Business Card</title>
<link rel="stylesheet" href="https://fonts.googleapis.com/css2?family=Tinos:wght@400&display=swap">
<style>
  :root {
    --page-bg: #ecebe8;
    --card-bg: #ffffff;
    --teal: #57b8ac;
    --teal-soft: #bfe4de;
    --ink: #1e1e1e;
    --grey: #5c5c5c;
  }
  * { margin: 0; padding: 0; box-sizing: border-box; }
  html, body {
    width: 1200px; height: 900px; overflow: hidden;
    background: var(--page-bg);
    font-family: "Tinos", "Times New Roman", serif;
  }
  .sheet {
    width: 1200px; height: 900px;
    display: flex; flex-direction: column; align-items: center; justify-content: center;
    gap: 56px;
  }
  .card {
    position: relative;
    width: 600px; height: 343px;
    background: var(--card-bg);
    box-shadow: 0 6px 18px rgba(0,0,0,0.14);
    overflow: hidden;
  }
  /* Front */
  .brand-name {
    position: absolute; left: 0; right: 0; top: 128px;
    text-align: center;
    color: var(--teal);
    font-size: 30px; letter-spacing: 1px;
  }
  .front-band {
    position: absolute; left: 0; right: 0; bottom: 0; height: 78px;
    background: linear-gradient(to bottom,
      var(--teal-soft) 0px, var(--teal) 8px, #ffffff 26px,
      #ffffff 52px, var(--teal) 72px, var(--teal-soft) 78px);
  }
  .front-web {
    position: absolute; left: 0; right: 0; bottom: 33px;
    text-align: center; font-size: 17px; color: var(--ink);
  }
  /* Back */
  .back-swoosh { position: absolute; inset: 0; }
  .back-contact {
    position: absolute; left: 28px; top: 26px;
    font-size: 13px; line-height: 1.35; color: var(--ink);
  }
  .back-brand {
    position: absolute; right: 40px; top: 26px;
    color: var(--teal); font-size: 15px;
  }
  .back-person {
    position: absolute; right: 36px; bottom: 40px; text-align: right;
  }
  .back-person .person-name { color: var(--teal); font-size: 19px; }
  .back-person .person-role { color: var(--ink); font-size: 13px; }
</style>
</head>
<body>
<main class="sheet">
  <section class="card card-front">
    <div class="brand-name">Selka Marven Photography</div>
    <div class="front-band"></div>
    <div class="front-web">www.yourcompany.com</div>
  </section>

  <section class="card card-back">
    <svg class="back-swoosh" width="600" height="343" viewBox="0 0 600 343" aria-hidden="true">
      <path d="M0 150 C 40 250, 140 320, 300 343 L 0 343 Z" fill="#111"/>
      <path d="M0 162 C 40 262, 130 326, 270 343 L 0 343 Z" fill="#57b8ac"/>
      <path d="M0 170 C 40 265, 125 326, 250 343" fill="none" stroke="#fff" stroke-width="3"/>
    </svg>
    <div class="back-contact">
      Suite 64<br>123 Street,<br>Tel: 1233 456<br>Mob: 1245 678<br>Email: yourname@yourcompany.com
    </div>
    <div class="back-brand">Selka Marven Photography</div>
    <div class="back-person">
      <div class="person-name">John Doe</div>
      <div class="person-role">Chief Executive Officer</div>
    </div>
  </section>
</main>
</body>
</html>
```